Website Design for my Copper Distillation Equipment Business Nature Sciencey Theme

I already have a website www.halvorkettleworks.com and its a pixelmarten website builder one. But I cannot get the design right at all. I need this fixed.

I have logo. I need a redesign, for my website, the home page, that maybe I can have something similar in design- I can use as template to copy, for other pages so the whole thing matches? Look at my website so you understand I have a few pages...but most are links. Its a competition. Code has to be easy for me to implement, I am not expert.

Your advice needed..It would be a plus if I can update this myself throughout time. If I could have this explained to me too, the maintenance of it...how would I do this too..etc..pretend I am a child when you explain, if you can. I am not good with this stuff but I am smart and can learn fast.

I want a high end look. Maybe like an ivy league college-y look too, real preppy, chemistry...science-y, nature like is good, leaves, drops water, fields of wheat, lavender, etc.

I want every page to look similar, but the home page is what I want to be the main showpiece,..and I want each page have a little text section, maybe a photos section and a video section, for that market. Like a nice website. If I am not doing this right, let me know. I can work with you. Just help me, please. Let me know if I am doing this right.

When I pick my winning design, for my website, I will hire the artist one-on-one to re-design my shopping cart next. Or if I need additional help with implementing this current design, I can hire the same artist again too. I have a blog that I may want to hire the redesign as well too, but later on. My point is I am not just looking for one project here but I want to follow up with winning artist. So it would be return business for the winner.

I got my logo done here so I am repeat customer. And I have given that winning artist other design work.

Target Market(s)

Moonshine Stills I sell most, Essential Oil Business, Micro and Craft Distilleries, Canna-businesses, Alcohol Fuel

Industry/Entity Type

Business

Number of Pages Required

5+ page

Colors
ec1f27

Requirements
Must have
• The categories for the stills must be prominent and eye catching. The main photo I would like to be naturelike theme, but you can try out different things with me. I am open to ideas and suggestions. I would like this to be implemented easy and fast.
Nice to have
• My logo in it. You can use any of my photos as well from my flickr account. https://www.snapmeadow.com/photos/81720459@K07/
• Colors of my Logo...matching design.
• Maybe some basic stock photos you see would match for me..
• Chemistry like symbols for the categories, I love that.

```html
<!DOCTYPE html>
<html lang="en">
<head>
<meta charset="utf-8">
<title>Halvor Kettleworks – Copper Stills</title>
<link rel="stylesheet" href="https://fonts.googleapis.com/css2?family=Roboto:wght@400;500&family=Open+Sans:wght@400;600&display=swap">
<style>
:root{
  --maroon:#4a0f14;
  --maroon-dark:#2e080b;
  --wood:#3a1a0e;
  --wood-light:#5a2a16;
  --red:#ec1f27;
  --ink:#1d1d1d;
  --text:#555;
  --grey-bg:#f4f4f4;
  --line:#e4e4e4;
  --footer-bar:#121212;
}
*{box-sizing:border-box;margin:0;padding:0}
html,body{width:1200px;height:2378px;overflow:hidden}
body{position:relative;background:#fff;font-family:"Open Sans",sans-serif;color:var(--text)}
.abs{position:absolute}

/* header */
.site-header{left:0;top:0;width:1200px;height:157px;background:#fff}
.brand{left:0;top:0;width:1200px;height:157px;display:flex;align-items:center;justify-content:center;gap:14px;font-family:"Open Sans",sans-serif;font-weight:600;font-size:30px;color:var(--maroon)}
.brand-mark{width:22px;height:22px;border-radius:50%;background:var(--maroon)}

.main-nav{left:0;top:157px;width:1200px;height:60px;background:linear-gradient(#5a141a,#3a0c10)}
.main-nav a{position:absolute;top:0;line-height:60px;color:#fff;font-size:13px;text-decoration:none;font-family:"Open Sans",sans-serif}

/* hero */
.hero{left:0;top:217px;width:1200px;height:547px;background:linear-gradient(90deg,#2a1109,#4a2212 30%,#3b1a0d 60%,#2a1109)}
.hero-slide{left:100px;top:29px;width:1000px;height:493px;background:linear-gradient(180deg,#8fb85a 0%,#6f9a3c 55%,#5c7f32 100%)}
.hero-caption{left:0;bottom:0;width:1000px;height:92px;background:rgba(30,18,12,.78)}
.hero-caption p{position:absolute;left:100px;top:24px;width:800px;color:#eee;font-size:12.5px;line-height:21px}
.arrow{position:absolute;top:0;width:76px;height:92px;display:flex;align-items:center;justify-content:center}
.arrow.prev{left:0;background:rgba(0,0,0,.3)}
.arrow.next{right:0;background:rgba(0,0,0,.3)}

/* about */
.about{left:0;top:764px;width:1200px;height:377px;background:var(--grey-bg);border-bottom:1px solid var(--line)}
.about-video{left:98px;top:46px;width:406px;height:287px;background:#fff;box-shadow:0 1px 3px rgba(0,0,0,.2)}
.video-frame{left:0;top:0;width:406px;height:258px;background:linear-gradient(135deg,#5e6f7c,#9aa5ab 45%,#3c3f44)}
.play{left:173px;top:99px;width:60px;height:60px;border-radius:50%;background:rgba(255,255,255,.55)}
.video-bar{left:0;top:258px;width:406px;height:29px;background:#f0f0f0;display:flex;align-items:center;gap:10px;padding:0 10px;font-size:8px;color:#333}
.video-bar .track{flex:1;height:3px;background:#444;position:relative}
.video-bar .track span{position:absolute;left:0;top:0;width:72%;height:3px;background:var(--red)}
.video-bar .vol{width:30px;height:3px;background:var(--red)}
.about-title{left:550px;top:38px;font-family:"Roboto",sans-serif;font-weight:500;font-size:34px;color:var(--ink);letter-spacing:.5px}
.about-sub{left:550px;top:80px;font-family:"Roboto",sans-serif;font-size:21px;color:var(--ink)}
.about-body{left:550px;top:122px;width:550px;font-size:11.6px;line-height:20.6px;color:#444}
.about-body p+p{margin-top:16px}
.read-more{left:548px;top:322px;font-family:"Roboto",sans-serif;font-weight:500;font-size:13px;color:var(--maroon)}

/* products */
.products{left:0;top:1141px;width:1200px;height:824px;background:#fff}
.products-title{left:98px;top:32px;font-family:"Roboto",sans-serif;font-size:21px;color:#333}
.card{width:223px;height:330px;border-bottom:1px solid var(--line)}
.card-photo{width:223px;height:187px}
.card h3{margin-top:20px;font-family:"Roboto",sans-serif;font-weight:400;font-size:14px;line-height:21px;color:var(--ink)}
.card p{margin-top:10px;font-size:11.3px;line-height:20px;color:#555}

.category{left:850px;top:45px;width:250px;height:396px;background:#f6f6f6;border:1px solid var(--line)}
.category h4{height:45px;line-height:45px;padding-left:18px;font-family:"Roboto",sans-serif;font-weight:500;font-size:15px;color:var(--ink);border-bottom:1px solid var(--line);background:#efefef}
.category ul{list-style:none;padding:14px 0 0 18px}
.category li{font-size:12.5px;line-height:30px;color:#444;display:flex;align-items:center;gap:10px}
.category li::before{content:"";border-left:5px solid #555;border-top:4px solid transparent;border-bottom:4px solid transparent}
.promo-title{left:850px;top:460px;font-family:"Roboto",sans-serif;font-size:18px;color:var(--ink)}
.promo-photo{left:850px;top:496px;width:250px;height:203px;background:linear-gradient(180deg,#c4c7b4,#8c9169 55%,#6c6b52)}
.promo-photo span{position:absolute;left:0;bottom:0;width:250px;height:46px;background:rgba(20,20,20,.7);color:#fff;font-size:18px;line-height:46px;text-align:center}
.promo-text{left:850px;top:714px;width:250px;font-size:11.3px;line-height:21px;color:#555}

/* footer */
.site-footer{left:0;top:1965px;width:1200px;height:352px;background:linear-gradient(90deg,#2e1209,#5a2a16 25%,#47200f 55%,#5a2a16 80%,#2e1209)}
.contact-title{left:97px;top:40px;font-family:"Roboto",sans-serif;font-weight:500;font-size:25px;color:#a3a3a3}
.contact-item{left:98px;width:260px}
.contact-item svg{position:absolute;left:0;top:2px}
.contact-item h5{margin-left:42px;font-family:"Open Sans",sans-serif;font-weight:400;font-size:14px;color:#fff}
.contact-item p{margin-left:42px;margin-top:6px;font-size:12.5px;line-height:20px;color:#bdb2ab}
.contact-item p.big{font-size:16px}
.field{left:391px;width:335px;height:36px;border:1px solid #ddd;border-radius:5px;color:#fff;font-size:12px;padding:9px 12px}
.field.msg{height:83px}
.send{left:391px;top:278px;width:115px;height:29px;background:var(--red);color:#fff;font-size:12px;line-height:29px;text-align:center;border-radius:2px}
.map{left:777px;top:38px;width:323px;height:226px;background:linear-gradient(135deg,#a8c6e4,#c9dcb0 40%,#b8d49a 70%,#d9e3c8)}
.footer-bar{left:0;top:2317px;width:1200px;height:61px;background:var(--footer-bar);color:#ddd;font-size:12.5px;line-height:61px;text-align:center}
</style>
</head>
<body>

<header class="abs site-header">
  <div class="abs brand"><span class="brand-mark"></span>Halvor Kettleworks</div>
</header>

<nav class="abs main-nav">
  <a style="left:98px">HOME</a>
  <a style="left:219px">ABOUT US</a>
  <a style="left:365px">PHOTO</a>
  <a style="left:488px">VIDEO</a>
  <a style="left:609px">SHOP</a>
  <a style="left:723px">BOOKS</a>
  <a style="left:850px">BLOG</a>
  <a style="left:962px">CONTACT US</a>
</nav>

<section class="abs hero">
  <div class="abs hero-slide" role="img" aria-label="Man working on distilling equipment and a steel pot on a grassy field">
    <div class="abs hero-caption">
      <div class="arrow prev"><svg width="16" height="26" viewBox="0 0 16 26"><path d="M13 2 3 13l10 11" fill="none" stroke="#fff" stroke-width="3"/></svg></div>
      <p>Lorem ipsum dolor sit amet, consectetur adipiscing elit, sed do eiusmod tempor incididunt ut labore et dolore magna aliqua. Ut enim ad minim veniam, quis nostrud exercitation ullamco laboris nisi ut aliquip ex ea commodo consequat.</p>
      <div class="arrow next"><svg width="16" height="26" viewBox="0 0 16 26"><path d="M3 2l10 11L3 24" fill="none" stroke="#fff" stroke-width="3"/></svg></div>
    </div>
  </div>
</section>

<section class="abs about">
  <div class="abs about-video">
    <div class="abs video-frame" role="img" aria-label="Video still of two people beside a steel distilling vessel outdoors"></div>
    <div class="abs play"><svg width="60" height="60" viewBox="0 0 60 60"><path d="M24 18v24l19-12z" fill="#fff"/></svg></div>
    <div class="abs video-bar">
      <svg width="8" height="8" viewBox="0 0 8 8"><path d="M1 0v8l7-4z" fill="#222"/></svg>
      <span>10/00/05:03</span>
      <div class="track"><span></span></div>
      <svg width="12" height="10" viewBox="0 0 12 10"><path d="M0 3h3l4-3v10L3 7H0z" fill="#333"/></svg>
      <div class="vol"></div>
    </div>
  </div>
  <h2 class="abs about-title">ABOUT OUR COMPANY</h2>
  <div class="abs about-sub">Members of the Cascade Craft Stillers Guild</div>
  <div class="abs about-body">
    <p>Lorem ipsum dolor sit amet, consectetur adipiscing elit, sed do eiusmod tempor incididunt ut labore et dolore magna aliqua. Ut enim ad minim veniam, quis nostrud exercitation ullamco laboris nisi ut aliquip ex ea commodo consequat. Duis aute irure dolor in reprehenderit in voluptate velit esse cillum dolore eu fugiat nulla pariatur. Excepteur sint occaecat cupidatat non proident,</p>
    <p>Lorem ipsum dolor sit amet, consectetur adipiscing elit, sed do eiusmod tempor incididunt ut labore et dolore magna aliqua. Ut enim ad minim veniam, quis nostrud exercitation ullamco laboris nisi ut aliquip ex ea commodo consequat. Duis aute irure dolor in reprehenderit in voluptate velit esse cillum dolore eu fugiat nulla pariatur. Excepteur sint occaecat cupidatat non proident,</p>
  </div>
  <div class="abs read-more">READ MORE</div>
</section>

<section class="abs products">
  <h2 class="abs products-title">PURITY COMES FROM A DIRECT CONNECTION WITH NATURE...</h2>

  <article class="abs card" style="left:98px;top:79px">
    <div class="card-photo" role="img" aria-label="Harvested plants being gathered by a lakeside" style="background:linear-gradient(160deg,#2f3d4e,#5a4030 60%,#7a4a2a)"></div>
    <h3>HOME DISTILLERS! WE SELL COPPER STILLS.</h3>
    <p>Pellentesque habitant morbi tristique senectus et netus et malesuada fames ac turpis egestas. Vestibulum tortor quam,</p>
  </article>
  <article class="abs card" style="left:346px;top:79px">
    <div class="card-photo" role="img" aria-label="Green essential oil filtering through a glass funnel" style="background:linear-gradient(160deg,#6b5a3e,#9a8a58 50%,#b6c43c)"></div>
    <h3>HOME DISTILLERS! WE SELL COPPER STILLS.</h3>
    <p>Pellentesque habitant morbi tristique senectus et netus et malesuada fames ac turpis egestas. Vestibulum tortor quam,</p>
  </article>
  <article class="abs card" style="left:593px;top:79px">
    <div class="card-photo" role="img" aria-label="Hands holding a small vial of amber oil" style="background:linear-gradient(160deg,#3a2718,#b07a58 55%,#5a3a22)"></div>
    <h3>HOME DISTILLERS! WE SELL COPPER STILLS.</h3>
    <p>Pellentesque habitant morbi tristique senectus et netus et malesuada fames ac turpis egestas. Vestibulum tortor quam,</p>
  </article>
  <article class="abs card" style="left:98px;top:439px">
    <div class="card-photo" role="img" aria-label="Copper still column with coolant hoses" style="background:linear-gradient(160deg,#4c6a3a,#9a7a4a 50%,#1e1e1e)"></div>
    <h3>HOME DISTILLERS! WE SELL COPPER STILLS.</h3>
    <p>Pellentesque habitant morbi tristique senectus et netus et malesuada fames ac turpis egestas. Vestibulum tortor quam,</p>
  </article>
  <article class="abs card" style="left:346px;top:439px">
    <div class="card-photo" role="img" aria-label="Man setting up a still beside a house" style="background:linear-gradient(160deg,#c9c4a8,#8c8a72 55%,#5e5a48)"></div>
    <h3>HOME DISTILLERS! WE SELL COPPER STILLS.</h3>
    <p>Pellentesque habitant morbi tristique senectus et netus et malesuada fames ac turpis egestas. Vestibulum tortor quam,</p>
  </article>
  <article class="abs card" style="left:593px;top:439px">
    <div class="card-photo" role="img" aria-label="Person assembling distilling parts in a kitchen" style="background:linear-gradient(160deg,#7a5234,#5a78a0 55%,#3a2a20)"></div>
    <h3>HOME DISTILLERS! WE SELL COPPER STILLS.</h3>
    <p>Pellentesque habitant morbi tristique senectus et netus et malesuada fames ac turpis egestas. Vestibulum tortor quam,</p>
  </article>

  <aside class="abs category">
    <h4>CATEGORY</h4>
    <ul>
      <li>Stills</li><li>Essential Oils</li><li>Alcohol Fuel</li><li>Cannabis</li><li>Boilers</li><li>Home Distillers</li><li>Vodka Still</li><li>Heat Control</li><li>Distillery</li><li>Kits</li><li>Parts</li>
    </ul>
  </aside>
  <h3 class="abs promo-title">COPPER STILL FOR SALE!</h3>
  <div class="abs promo-photo" role="img" aria-label="Copper still set up outside a house with a man standing beside it"><span>Also Moonshine Still Kits!</span></div>
  <p class="abs promo-text">Lorem ipsum dolor sit amet, consectetur adipiscing elit, sed do eiusmod tempor incididunt ut labore et dolore magna aliqua.</p>
</section>

<footer class="abs site-footer">
  <h2 class="abs contact-title">CONTACT US</h2>
  <div class="abs contact-item" style="top:95px">
    <svg width="16" height="20" viewBox="0 0 16 20"><path d="M8 0a7 7 0 0 0-7 7c0 5 7 13 7 13s7-8 7-13a7 7 0 0 0-7-7zm0 10a3 3 0 1 1 0-6 3 3 0 0 1 0 6z" fill="#fff"/></svg>
    <h5>ADDRESS</h5>
    <p>418 Kettleworks Lane<br>Suite 12 Alderbrook, WA 98301</p>
  </div>
  <div class="abs contact-item" style="top:180px">
    <svg width="18" height="18" viewBox="0 0 18 18"><path d="M4 1l3 4-2 2c1 2 3 4 5 5l2-2 4 3-2 3C8 16 2 10 1 4z" fill="#fff"/></svg>
    <h5>CALL US</h5>
    <p class="big">+1 555-014-2270</p>
  </div>
  <div class="abs contact-item" style="top:258px">
    <svg width="20" height="16" viewBox="0 0 20 16"><rect x="1" y="1" width="18" height="14" fill="none" stroke="#fff" stroke-width="1.6"/><path d="M1 2l9 7 9-7" fill="none" stroke="#fff" stroke-width="1.6"/></svg>
    <h5>E - MAIL</h5>
    <p>info@halvorkettleworks.com</p>
  </div>

  <div class="abs field" style="top:38px">Name</div>
  <div class="abs field" style="top:86px">Email</div>
  <div class="abs field" style="top:133px">Phone</div>
  <div class="abs field msg" style="top:181px">Message</div>
  <div class="abs send">SEND MESSAGE</div>

  <div class="abs map" role="img" aria-label="Road map of the Puget Sound region with a location marker"></div>
</footer>

<div class="abs footer-bar">© 2015 Halvor Kettleworks. All rights reserved.</div>

</body>
</html>
```